Business card with professional look

I would like a creative yet professional looking business card for our business. We sell broadcast TV related security products for mobile phones, set top boxes, and tablets. Our customers are international. We have a logo we like and I would like to possibly add some color to the business card but keep it professional looking.

Target Market(s)

Professionals in the TV, cable, ans Satellite industries

Industry/Entity Type

Cable Tv

Contact Information for Business Card

Name Ned Vastermill, title CEO, Address 8130 Harborline Court, Suite 400, Del Arvo, CA 91584 USA, phone numbers m:+1.619.284.7302 o:+1.855.672.9140, email, logo

Font styles to use
Other font styles liked:
• Open to any font that looks good with logo

Requirements
Must have
• professional look with colors coordinated with logo colors. would like to add one or two different colors as well as some form of background color

```html
<!DOCTYPE html>
<html lang="en">
<head>
<meta charset="utf-8">
<title>Vantacast Business Card</title>
<link href="https://fonts.googleapis.com/css2?family=Open+Sans:wght@400;600&display=swap" rel="stylesheet">
<style>
  :root {
    --page-bg: #d9d9d9;
    --card-bg: #e6f0dc;
    --panel-start: #0a88d2;
    --panel-end: #263a7c;
    --panel-text: #ffffff;
    --brand-grey: #58585a;
    --brand-blue: #0a7fcc;
  }
  * { margin: 0; padding: 0; box-sizing: border-box; }
  html, body {
    width: 1200px;
    height: 809px;
    overflow: hidden;
    background: var(--page-bg);
    font-family: "Open Sans", sans-serif;
  }
  .card {
    position: absolute;
    left: 40px;
    top: 72px;
    width: 1120px;
    height: 665px;
    background: var(--card-bg);
    box-shadow: 0 2px 6px rgba(0,0,0,0.15);
  }
  .contact-panel {
    position: absolute;
    left: 438px;
    top: 121px;
    width: 624px;
    height: 429px;
    border-radius: 28px;
    background: linear-gradient(90deg, var(--panel-start) 0%, var(--panel-start) 20%, var(--panel-end) 100%);
    color: var(--panel-text);
  }
  .person-name {
    position: absolute;
    right: 59px;
    top: 58px;
    font-size: 31px;
    font-weight: 400;
    white-space: nowrap;
  }
  .contact-row {
    position: absolute;
    left: 68px;
    display: flex;
    align-items: center;
    white-space: nowrap;
  }
  .contact-row svg {
    position: absolute;
    left: 0;
    fill: none;
    stroke: var(--panel-text);
    stroke-width: 2.4;
  }
  .contact-text { margin-left: 44px; }
  .address { top: 140px; font-size: 24px; line-height: 36px; }
  .address svg { top: 6px; }
  .mobile { top: 228px; font-size: 34px; }
  .office { top: 287px; font-size: 34px; }
  .email { top: 336px; font-size: 29px; }
  .brand {
    position: absolute;
    left: 61px;
    top: 540px;
    display: flex;
    align-items: center;
    gap: 14px;
  }
  .brand-name {
    font-size: 62px;
    font-weight: 600;
    color: var(--brand-grey);
    letter-spacing: -1px;
    line-height: 1;
  }
  .brand-mark {
    width: 26px;
    height: 26px;
    background: var(--brand-blue);
  }
</style>
</head>
<body>
  <div class="card">
    <div class="contact-panel">
      <div class="person-name">Ned Vastermill, CEO</div>

      <div class="contact-row address">
        <svg width="28" height="40" viewBox="0 0 28 40" aria-hidden="true">
          <path d="M14 37 C14 37 3 22 3 14 A11 11 0 0 1 25 14 C25 22 14 37 14 37 Z"/>
          <circle cx="14" cy="14" r="4.5"/>
        </svg>
        <div class="contact-text">8130 Harborline Court, Suite 400,<br>Del Arvo, CA 91584 USA</div>
      </div>

      <div class="contact-row mobile">
        <svg width="26" height="36" viewBox="0 0 26 36" aria-hidden="true">
          <rect x="4" y="2" width="18" height="32" rx="3"/>
          <line x1="4" y1="27" x2="22" y2="27"/>
          <line x1="11" y1="31" x2="15" y2="31"/>
        </svg>
        <div class="contact-text">+1.619.284.7302</div>
      </div>

      <div class="contact-row office">
        <svg width="30" height="36" viewBox="0 0 30 36" aria-hidden="true">
          <path d="M7 3 L12 3 L14 11 L10 14 C12 20 15 24 20 27 L23 23 L29 26 L28 32 C27 34 24 35 21 34 C12 30 5 20 3 10 C3 6 5 3 7 3 Z"/>
        </svg>
        <div class="contact-text">+1.855.672.9140</div>
      </div>

      <div class="contact-row email">
        <svg width="32" height="24" viewBox="0 0 32 24" aria-hidden="true">
          <rect x="2" y="2" width="28" height="20"/>
          <polyline points="2,2 16,14 30,2"/>
        </svg>
        <div class="contact-text">name@vantacast.com</div>
      </div>
    </div>

    <div class="brand">
      <span class="brand-name">Vantacast</span>
      <span class="brand-mark"></span>
    </div>
  </div>
</body>
</html>
```